Horticulture Consulting Company Premium Card

We are looking for new design for a premium business card.
Our cards will be printed on glossy and embossed premium card stock.

Target Market(s)

Horticulture business owners needing our consulting services

Contact Information for Business Card

Marcus Trell
(555) 304-2698
Marc@verdanilo.com

Requirements
Must have
• Company Logo and Contact information.
• Some additional work to add interest to the card
Should not have
• Red or Yellow

```html
<!DOCTYPE html>
<html lang="en">
<head>
<meta charset="utf-8">
<title>Verdanilo Solutions – Business Card</title>
<link rel="stylesheet" href="https://fonts.googleapis.com/css2?family=Montserrat:wght@800&family=Lato:wght@400;700&display=swap">
<style>
  :root {
    --scene-bg: #3a3a3a;
    --card-bg: #1f1f20;
    --card-edge: #2a2a2b;
    --emboss: #bdbdbd;
    --brand-green: #39b54a;
    --brand-blue: #1577c4;
    --text-light: #e6e6e6;
    --text-muted: #c9c9c9;
  }
  * { margin: 0; padding: 0; box-sizing: border-box; }
  html, body {
    width: 1200px; height: 900px; overflow: hidden;
    background: radial-gradient(ellipse at 70% 20%, #4a4a4a 0%, var(--scene-bg) 45%, #262626 100%);
    font-family: "Lato", sans-serif;
  }
  .card {
    position: absolute;
    left: 260px;
    width: 680px; height: 390px;
    background: var(--card-bg);
    box-shadow: 0 18px 40px rgba(0,0,0,.55);
    overflow: hidden;
  }
  .card--front { top: 45px; }
  .card--back { top: 465px; }

  /* front */
  .front-brand {
    position: absolute; inset: 0;
    display: flex; align-items: center; justify-content: center; gap: 22px;
  }
  .front-brand__mark {
    width: 74px; height: 74px; border-radius: 50%;
    background: #161617;
    box-shadow: inset 2px 2px 4px rgba(0,0,0,.7), inset -1px -1px 2px rgba(255,255,255,.08);
  }
  .front-brand__name {
    font-family: "Montserrat", sans-serif; font-weight: 800;
    font-size: 44px; letter-spacing: 1px; text-transform: uppercase;
    color: var(--emboss); line-height: 1.05;
  }

  /* back */
  .back-brand {
    position: absolute; left: 40px; top: 110px; width: 270px;
    display: flex; flex-direction: column; align-items: center; gap: 16px;
  }
  .back-brand__mark {
    width: 70px; height: 70px; border-radius: 50%;
    background: var(--brand-green);
  }
  .back-brand__name {
    font-family: "Montserrat", sans-serif; font-weight: 800;
    font-size: 27px; text-transform: uppercase; text-align: center;
    color: var(--brand-green); line-height: 1.1;
  }
  .divider { position: absolute; left: 345px; width: 2px; }
  .divider--blue { top: 95px; height: 60px; background: var(--brand-blue); }
  .divider--green { top: 200px; height: 90px; background: var(--brand-green); }

  .person { position: absolute; left: 385px; top: 100px; }
  .person__name {
    font-family: "Montserrat", sans-serif; font-weight: 800;
    font-size: 30px; letter-spacing: 1px; text-transform: uppercase;
    color: var(--brand-green);
  }
  .person__role { font-size: 18px; letter-spacing: 1px; color: var(--text-muted); margin-top: 2px; }

  .contact { position: absolute; left: 375px; top: 200px; list-style: none; }
  .contact__item {
    display: flex; align-items: center; gap: 14px;
    font-size: 20px; letter-spacing: 1px; color: var(--text-light);
    height: 32px;
  }
  .contact__icon { width: 18px; height: 18px; flex: none; fill: var(--brand-blue); }
  .contact__accent { color: var(--brand-green); }

  .edge-band { position: absolute; bottom: 0; height: 7px; width: 50%; }
  .edge-band--blue { left: 0; background: var(--brand-blue); }
  .edge-band--green { right: 0; background: var(--brand-green); }
</style>
</head>
<body>

<section class="card card--front" aria-label="Card front">
  <div class="front-brand">
    <span class="front-brand__mark" aria-hidden="true"></span>
    <span class="front-brand__name">Verdanilo<br>Solutions</span>
  </div>
</section>

<section class="card card--back" aria-label="Card back">
  <div class="back-brand">
    <span class="back-brand__mark" aria-hidden="true"></span>
    <span class="back-brand__name">Verdanilo<br>Solutions</span>
  </div>

  <span class="divider divider--blue" aria-hidden="true"></span>
  <span class="divider divider--green" aria-hidden="true"></span>

  <div class="person">
    <p class="person__name">Marcus Trell</p>
    <p class="person__role">Owner</p>
  </div>

  <ul class="contact">
    <li class="contact__item">
      <svg class="contact__icon" viewBox="0 0 18 18" aria-hidden="true">
        <rect x="4" y="1" width="10" height="16" rx="2"/>
        <rect x="6" y="3" width="6" height="8" fill="#1f1f20"/>
      </svg>
      (555) 304-2698
    </li>
    <li class="contact__item">
      <svg class="contact__icon" viewBox="0 0 18 18" aria-hidden="true">
        <rect x="1" y="4" width="16" height="11" rx="1"/>
        <path d="M1.5 4.5 L9 10 L16.5 4.5" fill="none" stroke="#1f1f20" stroke-width="1.5"/>
      </svg>
      Marc@verdanilo.com
    </li>
    <li class="contact__item">
      <svg class="contact__icon" viewBox="0 0 18 18" aria-hidden="true">
        <circle cx="9" cy="9" r="8"/>
        <g fill="none" stroke="#1f1f20" stroke-width="1.2">
          <ellipse cx="9" cy="9" rx="3.5" ry="8"/>
          <line x1="1" y1="9" x2="17" y2="9"/>
          <line x1="2.5" y1="5" x2="15.5" y2="5"/>
          <line x1="2.5" y1="13" x2="15.5" y2="13"/>
        </g>
      </svg>
      <span>www.<span class="contact__accent">verdanilo</span>.com</span>
    </li>
  </ul>

  <span class="edge-band edge-band--blue" aria-hidden="true"></span>
  <span class="edge-band edge-band--green" aria-hidden="true"></span>
</section>

</body>
</html>
```